Criação de Kit com 6 Layouts de Post para Redes Sociais (Facebook, Instagram e etc) + Capa de Facebook para Construção & Engenharia
" Atendemos principalmento sindicos de edificio "

```html
<!DOCTYPE html>
<html lang="pt-BR">
<head>
<meta charset="UTF-8">
<title>Antes e Depois – R. Tavares Engenharia</title>
<link rel="stylesheet" href="https://fonts.googleapis.com/css2?family=Montserrat:wght@300;800&family=Raleway:wght@400&display=swap">
<style>
  :root{
    --ink:#111111;
    --accent:#f5c21b;
    --paper:#ffffff;
    --room-wall:#eef0f2;
    --room-floor:#bfc3c7;
    --dark-panel:#2b2d30;
    --photo-top:#b9a9a4;
    --photo-mid:#7d4a5c;
    --photo-bottom:#23305f;
  }
  *{margin:0;padding:0;box-sizing:border-box}
  html,body{width:1200px;height:1200px;overflow:hidden;background:var(--paper)}
  .post{position:relative;width:1200px;height:1200px;overflow:hidden;
    font-family:"Montserrat",sans-serif;color:var(--ink)}
  .room-photo{position:absolute;inset:0;
    background:linear-gradient(180deg,var(--room-wall) 0%,var(--room-wall) 70%,var(--room-floor) 72%,#d9dcdf 100%)}
  .dark-panel{position:absolute;right:0;top:0;width:360px;height:1200px;background:var(--dark-panel)}
  .paint-splash{position:absolute;left:0;top:0;width:1200px;height:1200px}
  .worker-photo{position:absolute;left:630px;top:0;width:570px;height:1200px;
    background:linear-gradient(165deg,var(--photo-top) 0%,var(--photo-mid) 50%,var(--photo-bottom) 100%)}
  .headline{position:absolute;left:96px;top:100px;font-weight:800;font-size:108px;
    line-height:.98;letter-spacing:-1px;text-transform:uppercase}
  .headline .colon{color:var(--accent)}
  .subline{position:absolute;left:96px;top:326px;font-weight:300;font-size:58px;
    line-height:1.18;letter-spacing:-1px}
  .brand{position:absolute;left:60px;top:850px;width:480px;text-align:center;
    font-family:"Raleway",sans-serif;font-weight:400;color:var(--ink)}
  .brand-square{display:block;width:120px;height:120px;margin:0 auto 34px;background:var(--ink)}
  .brand-name{font-size:56px;letter-spacing:2px;line-height:1.1}
  .brand-tag{font-size:28px;letter-spacing:16px;margin-top:8px}
  .social{position:absolute;left:944px;top:1082px;display:flex;gap:34px}
  .social span{width:34px;height:34px;border-radius:50%;background:var(--paper)}
</style>
</head>
<body>
<main class="post">
  <div class="room-photo" role="img" aria-label="Ambiente interno claro com parede branca e piso cerâmico"></div>
  <div class="dark-panel"></div>
  <svg class="paint-splash" viewBox="0 0 1200 1200" role="img" aria-label="Mancha de tinta branca ao fundo">
    <path d="M460 0 H1010 L1080 180 C1010 300 1060 500 980 700 C900 900 760 1000 640 1060 C560 1000 470 980 420 900 C360 820 300 760 160 700 C90 670 40 620 0 600 V480 C120 520 260 520 360 440 C450 360 460 200 440 90 Z" fill="var(--paper)"/>
  </svg>
  <div class="worker-photo" role="img" aria-label="Foto de pintor de uniforme segurando rolo de pintura e fazendo sinal de positivo"></div>

  <h1 class="headline">Antes e<br>Depois<span class="colon">:</span></h1>
  <p class="subline">Nosso Trabalho<br>em Manutenção<br>Predial</p>

  <div class="brand">
    <span class="brand-square"></span>
    <div class="brand-name">R. TAVARES</div>
    <div class="brand-tag">ENGENHARIA</div>
  </div>

  <div class="social" aria-label="Redes sociais">
    <span></span><span></span><span></span>
  </div>
</main>
</body>
</html>
```